EmberMart, Charcoal bag packaging and brand

I'm looking at a package design for 10 KG/22 pounds of charcoal.
The design must include a name that is catchy and conveys quality, heat and low ash. The name must not violate any trademarks or tradenames. One of the best resources to view other packaging is the Grill Owl website. www.grillowl-example.com
Two colors only and one must be red which will be printed on a kraft paper bag. The name EMBERMART.COM must be prominent and also list our website of www.embermart-example.com.
Updates
Here is some wording for the front of the bag and it can be in any order. Make it look GREAT! Use the name "Blazewood Charcoal", but the Embermart logo should be the most prominant. Hi Heat, Low Ash, Long burning We will need some wording on the back and sides, but it's primarily just text and we won't worry about it until later. A UPC code will be necessary also. Thanks, Rick Tolliver
100% Natural Hardwood Lump Charcoal
Restaurant and Competition grade
No additives, No fillers
Non sparking
Easy lighting, use a chimney starter
Mild flavor profile
A number of the designs are using full coverage ink.
Please limit the amount of ink coverage to no more than 25% ..
It becomes very costly to use 100% coverage.
Thanks!
Rick Tolliver
Thank you to all the fine designers.
It was an extremely difficult decision for us. One fine designer was knocked out of the competition by our attorneys and we also received notice from the same attorneys that our brand of "Blazewood Charcoal" won't work...
I'll be posting another new logo design for branding of the charcoal at some point.
Kindest regards to all.
Rick Tolliver
Target Market(s)
End users, restaurants, resorts, competition cookoffs
Look and feel

```html
<!DOCTYPE html>
<html lang="en">
<head>
<meta charset="utf-8">
<title>Blazewood Charcoal – EmberMart bag front</title>
<link rel="stylesheet" href="https://fonts.googleapis.com/css2?family=Arimo:wght@700&display=swap">
<style>
  :root {
    --page: #ffffff;
    --kraft-light: #e3cdab;
    --kraft: #d8bd96;
    --kraft-dark: #cdb089;
    --brand-red: #c91d1f;
    --ink: #0d0d0d;
  }
  * { margin: 0; padding: 0; box-sizing: border-box; }
  html, body {
    width: 1200px; height: 900px; overflow: hidden;
    background: var(--page);
    font-family: "Arimo", Arial, sans-serif;
    font-weight: 700;
  }
  .bag-front {
    position: absolute; left: 292px; top: 0;
    width: 640px; height: 900px;
    background:
      radial-gradient(ellipse at 30% 20%, var(--kraft-light), transparent 60%),
      radial-gradient(ellipse at 75% 70%, var(--kraft-light), transparent 55%),
      linear-gradient(160deg, var(--kraft), var(--kraft-dark));
    overflow: hidden;
  }
  .band {
    position: absolute; left: 0; width: 100%;
    background: var(--brand-red);
    border-top: 7px solid var(--ink);
    border-bottom: 7px solid var(--ink);
  }
  .band--top { top: 17px; height: 83px; }
  .band--bottom { top: 684px; height: 174px; border-top-width: 9px; border-bottom-width: 8px; }
  .tagline {
    position: absolute; left: 78px; top: 20px;
    font-size: 24px; color: var(--ink); letter-spacing: 0.2px;
    word-spacing: 3px;
  }
  .brand-lockup {
    position: absolute; left: 0; top: 150px; width: 100%;
    display: flex; align-items: center; justify-content: center; gap: 22px;
  }
  .brand-lockup__dot {
    width: 70px; height: 70px; border-radius: 50%;
    background: var(--brand-red);
  }
  .brand-lockup__names { color: var(--brand-red); line-height: 1.05; }
  .brand-lockup__store { font-size: 74px; }
  .brand-lockup__product { font-size: 40px; }
  .benefits {
    position: absolute; left: 178px; top: 468px;
    list-style: none;
  }
  .benefits li {
    display: flex; align-items: center;
    height: 40px; font-size: 32px; color: var(--brand-red);
  }
  .benefits svg { width: 56px; height: 44px; margin-right: 16px; flex: none; }
  .features {
    position: absolute; left: 35px; top: 22px;
    list-style: none; font-size: 19px; color: var(--ink); line-height: 25.5px;
  }
</style>
</head>
<body>
  <main class="bag-front">
    <header class="band band--top">
      <p class="tagline">100% Natural Hardwood Lump Charcoal</p>
    </header>

    <div class="brand-lockup">
      <span class="brand-lockup__dot"></span>
      <div class="brand-lockup__names">
        <p class="brand-lockup__store">EmberMart</p>
        <p class="brand-lockup__product">Blazewood Charcoal</p>
      </div>
    </div>

    <ul class="benefits">
      <li><svg viewBox="0 0 56 44" aria-hidden="true"><path d="M2 24 L12 17 L20 28 L48 2 L54 6 L21 42 Z" fill="var(--ink)"/></svg>High Heat</li>
      <li><svg viewBox="0 0 56 44" aria-hidden="true"><path d="M2 24 L12 17 L20 28 L48 2 L54 6 L21 42 Z" fill="var(--ink)"/></svg>Low Ash</li>
      <li><svg viewBox="0 0 56 44" aria-hidden="true"><path d="M2 24 L12 17 L20 28 L48 2 L54 6 L21 42 Z" fill="var(--ink)"/></svg>Long Burning</li>
    </ul>

    <footer class="band band--bottom">
      <ul class="features">
        <li>Restaurant and Competition grade</li>
        <li>No additives, No fillers</li>
        <li>Non sparking</li>
        <li>Easy lighting, use a chimney starter</li>
        <li>Mild flavor profile</li>
      </ul>
    </footer>
  </main>
</body>
</html>
```